Veltrix Stationary

Design the stationary of Veltrix Promotions Group.

Veltrix is a BTL company, BTL meaning "below the line". In other words Veltrix is a Promotional Marketing company (the company that design the brands promotional activities).

The design should transmit creativity, agility, boldness.

I need:
* Bis Card
* Letter head
* Envelopes, both vertical and horizontal (for legal size), and letter envelope
* Folders
* PPT template (Title page and regular page)
* CD slip (CD envelope)
* ID card (employee card)

And what ever else you want to throw in.
Updates

Guys,

Something I missed from the brief.   The predominat color should be RED.

Also, have fun and play with the exclamation mark (!) of the logo. 

Hi guys, more comments:

Remember that Veltrix is a "creativity" agency, not in the advertising side but on the promotional side, and that should reflect on the stationary.

 I want a bold design.  Bold and yet crisp.

 

Guys, i just uploaded the Logo in AI format.

I Also uploaded the actual Veltrix Bis Card, wich I like.  So I will like to see some designs with that bis card approach.

Guys, I am so sorry, but I notice in your last post that I upladed a wrong design ("13154_marketing_group_veltrix_brief225630.ai").  The problem was that I asked the designer the file in AI format and he send me thw wrong file, and since I dont have Illustrator I could not verify it.

The differences are minor, I just already ask him the correct one (similar to the EPS file).

Sorry                                   

Just post the correct AI file : "Veltrix Logo.ai"

Reason: I'm expecting more designs to choose from and also I wont be available tomorrow to decide.

Reason: Sorry guys, but we are not there yet!

Target Market(s)

Marketing directors, Marketing Managers

Industry/Entity Type

Legal

Requirements
Must have
• Must work with the logo attached.
The predominat color should be RED.
Play and have fun with the exclamation mark (!).
Should not have
• * No old fonts

Should not be:
* boring
* Informal
* rigid

```html
<!DOCTYPE html>
<html lang="en">
<head>
<meta charset="utf-8">
<title>Veltrix Promotions Group – Stationery</title>
<link rel="stylesheet" href="https://fonts.googleapis.com/css2?family=Questrial&display=swap">
<style>
  :root {
    --red: #d7182a;
    --ink: #1b1b1b;
    --paper: #ffffff;
    --grey-text: #555555;
    --backdrop: #d9d9d9;
    --window: #f1f1f1;
    --font: "Questrial", "Century Gothic", sans-serif;
  }
  * { box-sizing: border-box; margin: 0; padding: 0; }
  html, body { width: 1200px; height: 808px; overflow: hidden; }
  body { background: var(--backdrop); font-family: var(--font); color: var(--ink); position: relative; }

  .sheet { position: absolute; background: var(--paper); box-shadow: 0 2px 8px rgba(0,0,0,.18); overflow: hidden; }

  .brand { font-family: var(--font); font-weight: 400; color: var(--ink); display: flex; align-items: center; gap: 6px; line-height: 1; }
  .brand .dot { display: inline-block; border-radius: 50%; background: var(--red); }
  .brand--light { color: var(--paper); }

  .band { position: absolute; left: 0; height: 14px; background: var(--ink); }
  .band-dot { position: absolute; border-radius: 50%; background: var(--red); border: 6px solid var(--ink); }

  .web { position: absolute; font-size: 8px; color: var(--paper); }
  .web b { font-weight: 400; }

  .contact { font-size: 7.5px; line-height: 1.45; color: var(--ink); }
  .contact .k { color: var(--red); }

  /* Letterhead */
  .letterhead { left: 20px; top: 20px; width: 520px; height: 768px; }
  .letterhead .brand { position: absolute; left: 60px; top: 110px; font-size: 34px; }
  .letterhead .brand .dot { width: 14px; height: 14px; }
  .letterhead .address { position: absolute; right: 70px; top: 70px; text-align: right; }
  .letter { position: absolute; left: 60px; top: 220px; width: 400px; font-size: 11px; line-height: 1.5; color: var(--grey-text); }
  .letter .date { margin-bottom: 20px; font-size: 12px; }
  .letter .recipient { margin-bottom: 26px; }
  .letter .recipient strong, .letter .sender strong { color: var(--ink); font-weight: 400; font-size: 12px; }
  .letter p { margin-bottom: 14px; text-align: justify; }
  .signature { width: 110px; height: 38px; background: #eeeeee; margin: 6px 0 10px; }
  .letterhead .band { bottom: 70px; width: 420px; }
  .letterhead .band-dot { left: 408px; bottom: 52px; width: 50px; height: 50px; }
  .letterhead .footer { position: absolute; left: 0; right: 0; bottom: 0; height: 24px; background: var(--ink); }
  .letterhead .web { left: 60px; bottom: 8px; }

  /* Business card front */
  .card-front { left: 560px; top: 20px; width: 290px; height: 165px; }
  .card-front .brand { position: absolute; left: 18px; top: 30px; font-size: 20px; }
  .card-front .brand .dot { width: 8px; height: 8px; }
  .card-front .person { position: absolute; right: 18px; top: 16px; text-align: right; font-size: 11px; color: var(--red); }
  .card-front .person span { display: block; font-size: 7.5px; color: var(--grey-text); }
  .card-front .contact { position: absolute; left: 18px; top: 92px; }
  .card-front .band { bottom: 26px; height: 9px; width: 240px; }
  .card-front .band-dot { left: 230px; bottom: 16px; width: 30px; height: 30px; border-width: 4px; }

  /* Business card back */
  .card-back { left: 880px; top: 20px; width: 290px; height: 165px; background: var(--ink); }
  .card-back .band-dot { left: 200px; top: 60px; width: 54px; height: 54px; border-color: var(--paper); }
  .card-back .web { left: 18px; bottom: 14px; }

  /* DL envelope front */
  .envelope { left: 560px; top: 205px; width: 620px; height: 290px; }
  .envelope .brand { position: absolute; left: 40px; top: 40px; font-size: 28px; }
  .envelope .brand .dot { width: 11px; height: 11px; }
  .envelope .window { position: absolute; left: 40px; top: 110px; width: 270px; height: 90px; border-radius: 18px; background: var(--window); border: 1px solid #e2e2e2; }
  .envelope .band { bottom: 56px; width: 530px; }
  .envelope .band-dot { left: 518px; bottom: 38px; width: 50px; height: 50px; }
  .envelope .footer { position: absolute; left: 0; right: 0; bottom: 0; height: 22px; background: var(--ink); }
  .envelope .web { left: 40px; bottom: 7px; }

  /* Envelope back */
  .envelope-back { left: 560px; top: 515px; width: 300px; height: 273px; }
  .envelope-back .flap { position: absolute; left: 0; top: 0; width: 300px; height: 150px; }
  .envelope-back .brand { position: absolute; left: 130px; top: 52px; font-size: 22px; }
  .envelope-back .brand .dot { width: 9px; height: 9px; }
  .envelope-back .contact { position: absolute; right: 18px; bottom: 22px; text-align: right; }

  /* Folder cover */
  .folder { left: 880px; top: 515px; width: 300px; height: 273px; }
  .folder .brand { position: absolute; left: 30px; top: 150px; font-size: 38px; }
  .folder .brand .dot { width: 16px; height: 16px; }
  .folder .tagline { position: absolute; left: 32px; top: 196px; font-size: 12px; letter-spacing: 4px; color: var(--ink); }
</style>
</head>
<body>

<section class="sheet letterhead" aria-label="Letterhead">
  <div class="contact address">
    123, Your Street, Your City,<br>Country, 123.<br>
    <span class="k">P</span> (123) 456 7890 &nbsp;<span class="k">F</span> (123) 456 7890<br>
    <span class="k">E</span> info@veltrix.com
  </div>
  <div class="brand">veltrix<span class="dot"></span></div>
  <div class="letter">
    <div class="date">March 4, 2011</div>
    <div class="recipient">
      <strong>Mr Daniel Reyes</strong><br>
      Managing Director<br>
      <strong>Northfield Capital</strong><br>
      48 Harbor Lane<br>
      Lakeview, WA 98012
    </div>
    <p>Lorem ipsum is simply placeholder text of the print and layout trade. It has stood in for real copy for many years, filling pages while the final words are written and approved by the team.</p>
    <p>Contrary to popular belief, lorem ipsum is not random text. It has roots in a piece of classical literature, and its first line comes from a section long studied by scholars of the period.</p>
    <p>Thank You for being one of our valued customers.</p>
    <div class="signature" role="img" aria-label="Handwritten signature"></div>
    <div class="sender">
      <strong>Marta Kessler</strong><br>
      President<br>
      Kessler Fabrication
    </div>
  </div>
  <div class="band"></div>
  <div class="band-dot"></div>
  <div class="footer"></div>
  <div class="web">www.<b>veltrix</b>.com</div>
</section>

<section class="sheet card-front" aria-label="Business card, front">
  <div class="brand">veltrix<span class="dot"></span></div>
  <div class="person">Your Name<span>Position</span></div>
  <div class="contact">
    123, Your Street, Your City, Country, 123.<br>
    <span class="k">P</span> (123) 456 7890 <span class="k">F</span> (123) 456 7890<br>
    <span class="k">E</span> info@veltrix.com <span class="k">W</span> www.veltrix.com
  </div>
  <div class="band"></div>
  <div class="band-dot"></div>
</section>

<section class="sheet card-back" aria-label="Business card, back">
  <div class="band-dot"></div>
  <div class="web">www.<b>veltrix</b>.com</div>
</section>

<section class="sheet envelope" aria-label="Window envelope">
  <div class="brand">veltrix<span class="dot"></span></div>
  <div class="window"></div>
  <div class="band"></div>
  <div class="band-dot"></div>
  <div class="footer"></div>
  <div class="web">www.<b>veltrix</b>.com</div>
</section>

<section class="sheet envelope-back" aria-label="Envelope, back">
  <svg class="flap" viewBox="0 0 300 150" aria-hidden="true">
    <path d="M0 0 H300 V70 C220 150 90 150 0 95 Z" fill="var(--ink)"/>
  </svg>
  <div class="brand brand--light">veltrix<span class="dot"></span></div>
  <div class="contact">
    123, Your Street, Your City, Country, 123.<br>
    <span class="k">P</span> (123) 456 7890 <span class="k">F</span> (123) 456 7890 <span class="k">E</span> info@veltrix.com
  </div>
</section>

<section class="sheet folder" aria-label="Folder cover">
  <div class="brand">veltrix<span class="dot"></span></div>
  <div class="tagline">PROMOTIONS GROUP</div>
</section>

</body>
</html>
```